Design website home page for pathology consulting company

Starting a new consulting company with anatomic pathologists focused on expert diagnosis and second opinions on difficult pathology cases. In the near future we will be incorporating next generation diagnostics for rare diseases of childhood into the business. These include discovery and testing of DNA for mutations.

The company is formed around one of the best known pathologists in the world named Marcus "Buddy" Halvorsen. The name of the company is "BuddyScope"

We had a logo design by Sketchfold - it is great. I will attach file as soon as I have it (contest ending today). Our company is medical, uses microscopes, DNA, probably will focus on childhood diseases but not solely on childhood diseases. we're not particularly conservative, but the customers we want to appeal to include older practicing pathologists as well as patients (sometimes parents) looking for second opinions.

Think a group of expert doctors diagnosing disease through the microscope and through DNA technology, ages ranging from 35-75 all trained by the best pathologist in the world - "Buddy"

We receive glass slides from diseases from patients all over the world from docs who need an expert to tell them what is the diagnosis. So "path to the diagnosis" is also part of the company marketing message.

We want the website design to describe our company but be very simple to find what one is looking for as we will use it as the launch page to:
1) order services
2) check results/reports
3) set up new account
4) speak with one of the pathologists
5) see our test menu
6) access our educational material/webinars

Update - looking for home page design and then finalists will ask for second page design to keep with theme - ok?

Reason: realized this project isn't web design but web home page design - thanks

Reason: Holidays for some in next two weeks

Reason: Hot discussion among collaborators for a few of the submissions. Will provide detail individually this weekend. Thanks so much for all the submissions!

Target Market(s)

Referring pathologists, physicians who want second opinions on pathology disease diagnosis, patients who have had biopsies (either patients themselves or parents of patients), generally high education level

Industry/Entity Type

Marketing

Requirements
Must have
• BuddyScope
Next Generation Pathology Consultants

```html
<!DOCTYPE html>
<html lang="en">
<head>
<meta charset="utf-8">
<title>BuddyScope – Next Generation Pathology Consultants</title>
<link href="https://fonts.googleapis.com/css2?family=PT+Serif&family=Roboto:wght@300;400;500&family=Open+Sans:wght@400;600&display=swap" rel="stylesheet">
<style>
:root{
  --blue:#0a6fb5;
  --blue-dark:#075a94;
  --text:#2b2b2b;
  --muted:#7b7f85;
  --page:#fbfcfc;
  --footer:#9a9da2;
  --footer-text:#e7e8ea;
  --footer-head:#5a5d62;
  --base:#5f6166;
  --field:#e6e6e6;
  --yellow-top:#fde27a;
  --yellow-bot:#f7b733;
}
*{box-sizing:border-box;margin:0;padding:0}
html,body{width:1029px;height:1200px;overflow:hidden}
body{background:var(--page);font-family:"Roboto",sans-serif;color:var(--text);position:relative}
.abs{position:absolute}
.top-rule{left:0;top:0;width:1029px;height:5px;background:var(--blue)}
.account-tab{left:620px;top:0;width:295px;height:27px;background:linear-gradient(var(--blue),var(--blue-dark));
  clip-path:polygon(0 0,100% 0,98% 100%,2% 100%);display:flex;justify-content:center;align-items:center;gap:22px;
  color:#fff;font-size:11.5px;font-weight:500}
.brand{left:127px;top:26px;width:130px;text-align:center}
.brand-mark{width:22px;height:22px;border-radius:50%;background:var(--blue);margin:0 auto 6px}
.brand-name{font-family:"PT Serif",serif;font-size:19px;color:var(--blue);letter-spacing:.5px}
.brand-tag{font-family:"Roboto",sans-serif;font-size:6.5px;color:var(--muted);margin-top:1px}
.contact-bar{left:454px;top:52px;display:flex;gap:18px;font-size:11px;color:var(--muted)}
.contact-bar span{display:flex;align-items:center;gap:5px}
.main-nav{left:424px;top:81px;width:482px;display:flex;justify-content:space-between;font-size:11px;font-weight:500;color:var(--blue);letter-spacing:.3px}
.main-nav i{font-style:normal}
.hero{left:0;top:113px;width:1029px;height:489px;
  background:linear-gradient(90deg,#e6eef5 0%,#eef3f7 35%,#c9dbe8 60%,#8fb2cc 80%,#d9e4ec 100%)}
.hero-title{left:129px;top:210px;font-family:"PT Serif",serif;font-size:42px;line-height:50px;color:var(--blue);font-weight:400}
.hero-copy{left:132px;top:321px;width:360px;font-size:15.5px;line-height:21.5px;font-weight:300;color:#444}
.consult{left:91px;top:506px;width:835px;height:186px;background:linear-gradient(#e6ebf1,#a8afb8)}
.consult-title{left:37px;top:24px;font-family:"PT Serif",serif;font-size:21px;line-height:25px;color:var(--blue)}
.consult-copy{left:37px;top:86px;width:230px;font-size:10.5px;line-height:15.5px;color:#333;font-family:"Open Sans",sans-serif}
.consult-divider{left:303px;top:21px;width:1px;height:146px;background:#8d949c}
.field{background:var(--field);border:1px solid #c6c9cd;font-size:10px;color:#777;padding:9px 10px}
.send{left:346px;top:135px;width:137px;height:31px;background:linear-gradient(var(--yellow-top),var(--yellow-bot));
  font-size:14px;font-weight:500;letter-spacing:.5px;color:#3a3a3a;display:flex;align-items:center;justify-content:center}
.card-title{font-family:"Open Sans",sans-serif;font-size:21.5px;color:var(--blue)}
.card-img{height:112px;margin-top:6px}
.card-copy{font-family:"Open Sans",sans-serif;font-size:10.4px;line-height:15.4px;color:#222;margin:17px 0 0 3px}
.read-more{display:inline-block;margin:15px 0 0 3px;font-family:"Open Sans",sans-serif;font-size:11px;font-weight:600;color:var(--blue-dark);text-decoration:underline}
.site-footer{left:0;top:1008px;width:1029px;height:150px;background:var(--footer)}
.footer-brand{left:116px;top:1040px;width:141px;text-align:center}
.footer-brand .brand-mark{width:32px;height:32px;background:#6c7075;margin-bottom:10px}
.footer-brand .brand-name{color:#5e6267;font-size:21px}
.footer-brand .brand-tag{color:#5e6267;font-size:7px}
.footer-col{top:1033px;font-size:10.5px;line-height:20.6px;color:var(--footer-text)}
.footer-col h4{font-weight:400;color:var(--footer-head);letter-spacing:.6px;font-size:10.5px}
.base-bar{left:0;top:1158px;width:1029px;height:42px;background:var(--base);border-top:2px solid #4e5055;
  display:flex;align-items:center;justify-content:center;font-size:11px;color:#d6d7d9;font-weight:500}
</style>
</head>
<body>
<div class="abs top-rule"></div>
<div class="abs account-tab"><span>Check Result</span><span>|</span><span>Login</span><span>|</span><span>Register</span></div>

<header>
  <div class="abs brand">
    <div class="brand-mark"></div>
    <div class="brand-name">BuddyScope</div>
    <div class="brand-tag">Next Generation Pathology Consultants</div>
  </div>
  <div class="abs contact-bar">
    <span><svg width="13" height="9" viewBox="0 0 13 9"><rect x=".5" y=".5" width="12" height="8" fill="none" stroke="#8a8e93"/><path d="M.5 .5 6.5 5 12.5 .5" fill="none" stroke="#8a8e93"/></svg>info@buddyscope.com</span>
    <span><svg width="12" height="12" viewBox="0 0 12 12"><circle cx="6" cy="6" r="5.4" fill="none" stroke="#8a8e93"/><path d="M6 3v3h2.5" fill="none" stroke="#8a8e93"/></svg>Monday-Friday: 8:00am-5:00pm</span>
    <span><svg width="13" height="13" viewBox="0 0 13 13"><path d="M3 1 5 4 3.8 5.4C4.6 7.2 5.8 8.4 7.6 9.2L9 8l3 2-1.2 2C6 11.6 1.4 7 1 2.2Z" fill="none" stroke="#8a8e93"/></svg>+1800 5550 1928</span>
  </div>
  <nav class="abs main-nav"><span>ORDER SERVICES</span><i>|</i><span>TEST MENU</span><i>|</i><span>WEBINARS</span><i>|</i><span>ABOUT</span><i>|</i><span>CONTACT US</span></nav>
</header>

<section>
  <div class="abs hero" role="img" aria-label="Photo of two pathologists in lab coats studying notes in a bright laboratory"></div>
  <h1 class="abs hero-title">EXPERT DISEASE<br>DIAGNOSIS</h1>
  <p class="abs hero-copy">Lorem ipsum dolor sit amet, consectetur adipisicing elit, sed do eiusmod tempor incididunt ut labore et dolore magna aliqua.</p>
</section>

<section class="abs consult">
  <h2 class="abs consult-title">CONSULT WITH ONE<br>OF THE PATHOLOGISTS</h2>
  <p class="abs consult-copy">Lorem ipsum dolor sit amet, consectetur adipisicing elit, sed do eiusmod tempor incidi-dunt ut labore et dolore magna aliqua.</p>
  <div class="abs consult-divider"></div>
  <div class="abs field" style="left:345px;top:19px;width:137px;height:29px">Enter your name..</div>
  <div class="abs field" style="left:493px;top:19px;width:137px;height:29px">Enter your email..</div>
  <div class="abs field" style="left:637px;top:19px;width:137px;height:29px">Enter your phone..</div>
  <div class="abs field" style="left:345px;top:57px;width:429px;height:66px">Enter your email..</div>
  <div class="abs send">SEND EMAIL</div>
</section>

<section>
  <article class="abs" style="left:102px;top:714px;width:266px">
    <h3 class="card-title">Our Services</h3>
    <div class="card-img" role="img" aria-label="Photo of a scientist pipetting samples at a microscope" style="background:linear-gradient(90deg,#9cc0da,#dfe9f1 45%,#3f6f9a 80%,#aac6dc)"></div>
    <p class="card-copy">Lorem ipsum dolor sit amet, consectetur adipisicing elit, sed do eiusmod tempor incididunt ut labore et dolore magna aliqua. Ut enim ad minim veniam, quis nostrud exercitation.</p>
    <span class="read-more">READ MORE</span>
  </article>
  <article class="abs" style="left:386px;top:714px;width:256px">
    <h3 class="card-title">Test Menu</h3>
    <div class="card-img" role="img" aria-label="Photo of test tubes filled with blue and orange liquid" style="background:linear-gradient(#f3c58a,#f0a24a 40%,#4aa0e0 70%,#1f6fd0)"></div>
    <p class="card-copy">Lorem ipsum dolor sit amet, consectetur adipisicing elit, sed do eiusmod tempor incididunt ut labore et dolore magna aliqua. Ut enim ad minim veniam, quis nostrud exercitation.</p>
    <span class="read-more">READ MORE</span>
  </article>
  <article class="abs" style="left:659px;top:714px;width:266px">
    <h3 class="card-title">Webinars</h3>
    <div class="card-img" role="img" aria-label="Photo of a brain scan display beside a masked lab researcher" style="background:linear-gradient(90deg,#cfe3ec,#b7d4e2 50%,#e4ecef 75%,#d8dfe3)"></div>
    <p class="card-copy">Lorem ipsum dolor sit amet, consectetur adipisicing elit, sed do eiusmod tempor incididunt ut labore et dolore magna aliqua. Ut enim ad minim veniam, quis nostrud exercitation.</p>
    <span class="read-more">READ MORE</span>
  </article>
</section>

<footer>
  <div class="abs site-footer"></div>
  <div class="abs footer-brand">
    <div class="brand-mark"></div>
    <div class="brand-name">BuddyScope</div>
    <div class="brand-tag">Next Generation Pathology Consultants</div>
  </div>
  <div class="abs footer-col" style="left:382px"><h4>NAVIGATION</h4>Home<br>Order Services<br>Testu Menu<br>Webinars</div>
  <div class="abs footer-col" style="left:543px"><h4>ABOUT US</h4>Login<br>Register<br>Check Results<br>Contact Us</div>
  <div class="abs footer-col" style="left:697px"><h4>CONTACT US</h4>Phone : +61 3 555 0192<br>Email: info@buddyscope.com<br>Your Street, Your Avenue<br>Your Country, 10001</div>
  <div class="abs base-bar">© Copyright 2013 BuddyScope. All Right Reserved | Privacy Policy | Site Map</div>
</footer>
</body>
</html>
```